Healthcare technology firm needs business card layout. Logo provided.

We need a business card design for a new healthcare technology company called Kevrimo.com. The logo is already done so that will be used in the design. We assist patients and their families manage their personal health finances. Our initial product is our web site membership that includes educational content on your health benefits, tools, and downloadable forms.

We would like to see designs that use our existing logo or extend the logo in a creative way. Should be very consumer friendly.

```html
<!DOCTYPE html>
<html lang="en">
<head>
<meta charset="utf-8">
<title>Kevrimo.com – Business Card</title>
<link rel="stylesheet" href="https://fonts.googleapis.com/css2?family=Poiret+One&display=swap">
<style>
  :root {
    --blue-light: #33a3f7;
    --blue-dark: #1a55e0;
    --blue-mark: #1f6fe6;
    --green: #66ff1a;
    --green-soft: #5cf21a;
    --cyan: #2cc4f2;
    --grey-strip: #e4e4e4;
    --white: #ffffff;
    --font: "Poiret One", sans-serif;
  }
  * { margin: 0; padding: 0; box-sizing: border-box; }
  html, body { width: 1200px; height: 716px; overflow: hidden; background: var(--white); }
  .card {
    position: relative;
    width: 1200px;
    height: 716px;
    font-family: var(--font);
    background: var(--white);
    overflow: hidden;
  }
  .band { position: absolute; left: 0; width: 1200px; }
  .band-top { top: 0; height: 42px; display: flex; }
  .band-top .half-blue { width: 600px; background: linear-gradient(180deg, var(--blue-light), var(--blue-dark)); }
  .band-top .half-green { width: 600px; background: var(--green); }
  .strip { position: absolute; left: 0; width: 1200px; background: var(--grey-strip); }
  .strip-top { top: 42px; height: 28px; }
  .strip-bottom { top: 408px; height: 29px; }

  .wordmark {
    position: absolute;
    top: 92px;
    left: 0;
    width: 1200px;
    text-align: center;
    font-size: 172px;
    line-height: 1;
    letter-spacing: 14px;
    color: var(--blue-mark);
    font-weight: 400;
  }
  .tagline {
    position: absolute;
    top: 340px;
    left: 0;
    width: 1200px;
    text-align: center;
    font-size: 48px;
    color: var(--cyan);
  }

  .band-bottom { top: 437px; height: 279px; display: flex; }
  .band-bottom .half-blue { width: 600px; background: linear-gradient(180deg, var(--blue-light), var(--blue-dark)); }
  .band-bottom .half-green { width: 600px; background: var(--green-soft); }

  .contact-text {
    position: absolute;
    color: var(--white);
    text-align: center;
    line-height: 1;
    white-space: nowrap;
  }
  .person-name { top: 474px; left: 40px; width: 540px; font-size: 60px; }
  .person-title { top: 540px; left: 40px; width: 540px; font-size: 60px; }
  .person-phone { top: 630px; left: 40px; width: 540px; font-size: 40px; }
  .locations { top: 476px; left: 650px; width: 540px; font-size: 45px; line-height: 54px; }
  .website { top: 632px; left: 650px; width: 540px; font-size: 46px; }

  .divider-dot { position: absolute; left: 556px; width: 88px; height: 88px; }
  .dot-upper { top: 463px; }
  .dot-lower { top: 603px; }
</style>
</head>
<body>
<main class="card">
  <div class="band band-top"><div class="half-blue"></div><div class="half-green"></div></div>
  <div class="strip strip-top"></div>

  <h1 class="wordmark">KEVRIMO</h1>
  <p class="tagline">Making your health costs clearer</p>

  <div class="strip strip-bottom"></div>
  <div class="band band-bottom"><div class="half-blue"></div><div class="half-green"></div></div>

  <svg class="divider-dot dot-upper" viewBox="0 0 88 88" aria-hidden="true">
    <defs>
      <linearGradient id="ringBlue" x1="0" y1="0" x2="0" y2="1">
        <stop offset="0" stop-color="#3aa8f8"/>
        <stop offset="1" stop-color="#1a4fdc"/>
      </linearGradient>
    </defs>
    <circle cx="44" cy="44" r="43" fill="url(#ringBlue)"/>
    <circle cx="42" cy="45" r="35" fill="#ffffff"/>
  </svg>
  <svg class="divider-dot dot-lower" viewBox="0 0 88 88" aria-hidden="true">
    <circle cx="44" cy="44" r="43" fill="url(#ringBlue)"/>
    <circle cx="42" cy="45" r="35" fill="#ffffff"/>
  </svg>

  <p class="contact-text person-name">Dana M. Corliss</p>
  <p class="contact-text person-title">CEO</p>
  <p class="contact-text person-phone">Mobile: 239-555-0147</p>

  <p class="contact-text locations">Carrow Bay, Linden Falls<br>Merriton, Ashford Vale</p>
  <p class="contact-text website">www.kevrimo.com</p>
</main>
</body>
</html>
```